Price Package PDF - 2 page PDF of stylized price packages for property management firm

Looking for a 2 x A4 page PDF for our two price packages.
I would like this to be in similar style to our website www.harbourlanerentals.com.au
I have attached an example. But would like mine to be a little more stylish and modern, preferably using design similar to our website.
Words and images also attached

Target Market(s)

investment property owners, male and female, aged 30-60

Industry/Entity Type

Real Estate

Font styles to use
Sans Serif

Requirements
Must have
• split two packages onto seperate A4 pages (See example file attached)
• Contact info:
• Website: www.harbourlanerentals.com.au
• email: info@harbourlanerentals.com.au
• Phone: Tom Radley 0417 562 903, Larisa Okonjo 0409 317 648
• Office Address: Suite 7, 12-14 Wattle Parade, Curl Curl NSW 2096
Nice to have
• I would like to use any of the pictures provided or images of modern residential property interior or of Sydney's Northern Beaches.

```html
<!DOCTYPE html>
<html lang="en">
<head>
<meta charset="utf-8">
<title>Harbour Lane Rentals – Price Packages</title>
<link href="https://fonts.googleapis.com/css2?family=Lato:wght@300;400;700&display=swap" rel="stylesheet">
<style>
:root{
  --board:#ececed;
  --page:#ffffff;
  --ink:#222629;
  --muted:#4a4f54;
  --teal:#1a8a9a;
  --footer:#363a40;
  --footer-text:#c9ccd0;
  --white:#ffffff;
}
*{box-sizing:border-box;margin:0;padding:0}
html,body{width:1200px;height:960px;overflow:hidden}
body{background:var(--board);font-family:'Lato',sans-serif;color:var(--ink);position:relative}
.page{position:absolute;top:116px;width:510px;height:723px;background:var(--page);display:flex;flex-direction:column}
.page--all{left:52px}
.page--lease{left:638px}
.hero{position:relative;height:229px;flex:none}
.hero-photo{position:absolute;inset:0}
.page--all .hero-photo{background:linear-gradient(180deg,#2d6f93 0%,#4f97b6 45%,#b8c7c2 62%,#1f5f8a 72%,#123f6a 100%)}
.page--lease .hero-photo{background:linear-gradient(180deg,#6d98b0 0%,#a9c4d1 35%,#44788c 47%,#3f8a8e 65%,#5aa4a3 100%)}
.brand{position:absolute;top:40px;left:0;right:0;text-align:center;color:var(--white);font-weight:700;font-size:20px;letter-spacing:.3px}
.hero-title{position:absolute;left:0;right:0;text-align:center;color:var(--white);font-weight:400;font-size:29px;line-height:33px;letter-spacing:.2px}
.page--all .hero-title{top:104px}
.page--lease .hero-title{top:105px}
.includes{height:132px;flex:none;position:relative;padding:11px 0 0 37px;display:flex}
.includes-heading{font-weight:300;font-size:17px;letter-spacing:.5px;width:109px;margin-top:1px}
.includes-list{list-style:none;font-size:8.2px;line-height:12px;color:var(--ink)}
.includes-list li{position:relative;padding-left:7px}
.includes-list li::before{content:"•";position:absolute;left:0}
.includes-list--first{width:148px}
.feature{position:relative;height:298px;flex:none}
.feature-photo{position:absolute;inset:0}
.page--all .feature-photo{background:linear-gradient(180deg,#5fb0dc 0%,#a9d2ea 28%,#8a8f90 45%,#5d7458 70%,#3f6a34 100%)}
.page--lease .feature-photo{background:linear-gradient(180deg,#2c93d6 0%,#6cb7e4 25%,#5b6166 45%,#4c7a3c 68%,#8c9890 100%)}
.rates{position:absolute;left:266px;top:72px;width:207px;height:154px;background:rgba(255,255,255,.93);padding:7px 0 0 7px}
.rates-heading{font-weight:300;font-size:16px;letter-spacing:.4px;margin-bottom:8px}
.rates-table{border-collapse:collapse;font-size:7.4px;color:var(--ink)}
.rates-table th{font-weight:400;text-align:left;width:90px;vertical-align:top;padding:0 0 7.5px}
.rates-table td{font-weight:700;vertical-align:top;padding:0 0 7.5px;line-height:9px}
.rate-big{color:var(--teal);font-size:12px;font-weight:400}
.rate-gst{color:var(--teal);font-weight:400}
.footer{flex:1;background:var(--footer);color:var(--footer-text);display:flex;justify-content:space-between;align-items:center;padding:0 37px}
.footer-contact{font-size:6.3px;line-height:9.4px}
.footer-web{color:var(--white);font-weight:700;font-size:7.8px}
</style>
</head>
<body>

<section class="page page--all">
  <header class="hero">
    <div class="hero-photo" role="img" aria-label="Photo of a harbour bay with moored boats and waterfront apartments"></div>
    <div class="brand">HARBOUR LANE RENTALS</div>
    <h1 class="hero-title">ALL INCLUSIVE PACKAGE</h1>
  </header>
  <div class="includes">
    <h2 class="includes-heading">INCLUDES</h2>
    <ul class="includes-list includes-list--first">
      <li>Securing Tenant</li>
      <li>Reference/Database Checking</li>
      <li>Lease Preparation and Signing</li>
      <li>Direct Debit rent collection</li>
      <li>Zero arrears policy management</li>
      <li>Payment of Rates and levies</li>
      <li>Insurance management</li>
      <li>Coordination or all repairs<br>and maintenance</li>
    </ul>
    <ul class="includes-list">
      <li>Regular rent reviews and renewals</li>
      <li>Detailed ingoing, ongoing and outgoing<br>inspections with photos and videos – viewable<br>through your personal Landlord portal</li>
      <li>Bond management – lodging and refunding</li>
      <li>Electronic monthly and EOFY statements</li>
      <li>Annual scheduled maintenance report</li>
      <li>Regulation/compliance management</li>
      <li>Tribunal Representation</li>
    </ul>
  </div>
  <div class="feature">
    <div class="feature-photo" role="img" aria-label="Photo of modern townhouses with garden terraces and stairs"></div>
    <div class="rates">
      <h3 class="rates-heading">ALL INCLUSIVE PACKAGE</h3>
      <table class="rates-table">
        <tr><th>Management Rate</th><td><span class="rate-big">10%</span> <span class="rate-gst">+ GST</span> of rental income</td></tr>
        <tr><th>Letting Fee</th><td>No Charge</td></tr>
        <tr><th>Advertising</th><td>No Charge</td></tr>
        <tr><th>Professional Photography</th><td>$199 (inc GST) 4 x Photos</td></tr>
        <tr><th>Statements:</th><td>No Charge</td></tr>
        <tr><th>Lease Preperation</th><td>No Charge</td></tr>
        <tr><th>Renewal Fees</th><td>No Charge</td></tr>
      </table>
    </div>
  </div>
  <footer class="footer">
    <p class="footer-contact">Office: Suite 7, 12-14 Wattle Parade, Curl Curl NSW 2096<br>Tom Radley 0417 562 903 &nbsp;|&nbsp; Larisa Okonjo 0409 317 648<br>info@harbourlanerentals.com.au</p>
    <p class="footer-web">www.harbourlanerentals.com.au</p>
  </footer>
</section>

<section class="page page--lease">
  <header class="hero">
    <div class="hero-photo" role="img" aria-label="Photo of a calm ocean rock pool with a distant headland"></div>
    <div class="brand">HARBOUR LANE RENTALS</div>
    <h1 class="hero-title">LEASE AND MANAGEMENT<br>PACKAGE</h1>
  </header>
  <div class="includes">
    <h2 class="includes-heading">INCLUDES</h2>
    <ul class="includes-list includes-list--first">
      <li>Securing Tenant</li>
      <li>Reference/Database Checking</li>
      <li>Lease Preparation and Signing</li>
      <li>Direct Debit rent collection</li>
      <li>Zero arrears policy management</li>
      <li>Payment of Rates and levies</li>
      <li>Insurance management</li>
      <li>Coordination or all repairs<br>and maintenance</li>
    </ul>
    <ul class="includes-list">
      <li>Regular rent reviews and renewals</li>
      <li>Detailed ingoing, ongoing and outgoing<br>inspections with photos and videos – viewable<br>through your personal Landlord portal</li>
      <li>Bond management – lodging and refunding</li>
      <li>Electronic monthly and EOFY statements</li>
      <li>Annual scheduled maintenance report</li>
      <li>Regulation/compliance management</li>
      <li>Tribunal Representation</li>
    </ul>
  </div>
  <div class="feature">
    <div class="feature-photo" role="img" aria-label="Photo of a modern two-storey house with balcony and lush garden"></div>
    <div class="rates">
      <h3 class="rates-heading">MANAGEMENT RATE</h3>
      <table class="rates-table">
        <tr><th>Management Rate</th><td><span class="rate-big">6%</span> <span class="rate-gst">+ GST</span> of rental income</td></tr>
        <tr><th>Letting Fee</th><td>1 weeks rent +GST 6<br>or 12 month lease</td></tr>
        <tr><th>Advertising</th><td>$350 (Inc GST)</td></tr>
        <tr><th>Professional Photography</th><td>$199 (inc GST) 4 x Photos</td></tr>
        <tr><th>Statements:</th><td>$5.00 Per month</td></tr>
        <tr><th>Lease Preperation</th><td>No Charge</td></tr>
        <tr><th>Renewal Fees</th><td>½ Weeks Rent +GST</td></tr>
      </table>
    </div>
  </div>
  <footer class="footer">
    <p class="footer-contact">Office: Suite 7, 12-14 Wattle Parade, Curl Curl NSW 2096<br>Tom Radley 0417 562 903 &nbsp;|&nbsp; Larisa Okonjo 0409 317 648<br>info@harbourlanerentals.com.au</p>
    <p class="footer-web">www.harbourlanerentals.com.au</p>
  </footer>
</section>

</body>
</html>
```